Business Card Design Project

New business cards that encompass our new logo.
Looking for -
Name, Title, Cell Phone, Email, Address (2 lines), Main Phone, Fax, and website.
Reason: I don't like the graphics used to show phone, fax, cell, email, web, and address.....
I like the double sided cards with logo's on the back. I do not like the logos for phone, fax, cell, address, email, or web.

```html
<!DOCTYPE html>
<html lang="en">
<head>
<meta charset="utf-8">
<title>Northpeak Supply – Business Card</title>
<link rel="stylesheet" href="https://fonts.googleapis.com/css2?family=Open+Sans:wght@400;600;700&display=swap">
<style>
  :root {
    --backdrop: #3b3b3b;
    --card: #ffffff;
    --accent-red: #c8394c;
    --brand-blue: #1f4c91;
    --text-grey: #4a4a4a;
    --rule: #d9d9d9;
  }
  html, body {
    margin: 0;
    padding: 0;
    width: 1200px;
    height: 720px;
    overflow: hidden;
    background: var(--backdrop);
    font-family: "Open Sans", Arial, sans-serif;
  }
  .business-card {
    position: absolute;
    left: 100px;
    top: 75px;
    width: 1000px;
    height: 570px;
    background: var(--card);
    overflow: hidden;
    box-shadow: 0 10px 30px rgba(0,0,0,0.45);
  }
  .card-shapes {
    position: absolute;
    inset: 0;
  }
  .brand-name {
    position: absolute;
    left: 60px;
    top: 225px;
    width: 380px;
    margin: 0;
    text-align: center;
    color: var(--brand-blue);
    font-weight: 700;
    font-size: 50px;
    line-height: 1.05;
    letter-spacing: 1px;
    text-transform: uppercase;
  }
  .contact-block {
    position: absolute;
    left: 560px;
    top: 72px;
    color: var(--text-grey);
  }
  .person-name {
    margin: 0;
    color: var(--brand-blue);
    font-weight: 700;
    font-size: 30px;
    line-height: 1.1;
  }
  .person-title {
    margin: 2px 0 0;
    color: var(--accent-red);
    font-weight: 600;
    font-size: 20px;
  }
  .address {
    margin: 22px 0 0;
    font-size: 18px;
    line-height: 1.35;
  }
  .contact-list {
    list-style: none;
    margin: 20px 0 0;
    padding: 0;
    font-size: 19px;
    line-height: 1.5;
  }
  .contact-list li {
    display: flex;
    align-items: baseline;
  }
  .contact-label {
    width: 28px;
    flex: none;
    color: var(--accent-red);
    font-weight: 700;
    font-size: 17px;
  }
  .website {
    position: absolute;
    right: 52px;
    bottom: 46px;
    margin: 0;
    color: #ffffff;
    font-weight: 600;
    font-size: 19px;
    letter-spacing: 4px;
  }
</style>
</head>
<body>
  <div class="business-card">
    <svg class="card-shapes" width="1000" height="570" viewBox="0 0 1000 570" aria-hidden="true">
      <polygon points="0,0 560,0 0,130" fill="var(--accent-red)"/>
      <polygon points="1000,330 1000,570 200,570" fill="var(--accent-red)"/>
      <line x1="470" y1="70" x2="500" y2="400" stroke="var(--rule)" stroke-width="2"/>
    </svg>

    <p class="brand-name">Northpeak<br>Supply</p>

    <div class="contact-block">
      <h1 class="person-name">Daniel Reyes</h1>
      <p class="person-title">Director</p>
      <p class="address">Suite 410 Harbor Road,<br>Juneau, AK 99801</p>
      <ul class="contact-list">
        <li><span class="contact-label">P</span>907 555 0142</li>
        <li><span class="contact-label">C</span>907 555 0187</li>
        <li><span class="contact-label">F</span>907 555 0193</li>
        <li><span class="contact-label">E</span>hello@northpeaksupply.com</li>
      </ul>
    </div>

    <p class="website">www.northpeaksupply.com</p>
  </div>
</body>
</html>
```